Hot-air ballooning company needs a DL-size flyer

Skylark Aerial Tours is a hot-air ballooning company which flies passengers in the King Valley, Victoria, Australia.
We need a 2-sided DL-size flyer which promotes our hot-air balloon flights and packages.
Most of our customers are couples, and we want the flyer design to communicate safety, adventure, and romance.
The flyer should make the best use of our images which we provide, and we've also included a document with the text for the flyer.
Updates

2 days is not long enough to gather designs, the brief never asked me what my deadline should be.

Target Market(s)

Couples, buyers are majority female, between the ages of 20-60

Industry/Entity Type

Tourism

Font styles to use
Sans Serif

Colors

Designer to choose colors to be used in the design.

Requirements
Must have
• Communicate safety, adventure, and romance
• Use images
Nice to have
• There is a lot of text, it would be great if you could make it look like as little text as possible
Should not have
• No childish designs

```html
<!DOCTYPE html>
<html lang="en">
<head>
<meta charset="utf-8">
<title>Skylark Aerial Tours – Your Flight</title>
<link href="https://fonts.googleapis.com/css2?family=Khand:wght@400;500;700&display=swap" rel="stylesheet">
<style>
  :root {
    --ink: #1f1f1f;
    --navy: #16288a;
    --panel: #e8f1fa;
    --paper: #ffffff;
    --icon: #333333;
  }
  * { margin: 0; padding: 0; box-sizing: border-box; }
  html, body { width: 1200px; height: 2400px; overflow: hidden; background: var(--paper); }
  body { font-family: "Khand", "Arial Narrow", sans-serif; color: var(--ink); }
  .flyer { position: relative; width: 1200px; height: 2400px; overflow: hidden; background: var(--paper); }

  .heading {
    position: absolute; left: 131px; top: 68px;
    font-size: 48px; font-weight: 700; letter-spacing: 0.5px; line-height: 1;
  }
  .feature { position: absolute; display: flex; align-items: center; gap: 16px; font-size: 22px; font-weight: 500; line-height: 1; white-space: nowrap; }
  .feature svg { width: 32px; height: 32px; flex: none; }

  .photo-band { position: absolute; left: 0; top: 456px; width: 1200px; height: 517px; }
  .panel-list .feature { font-size: 22px; }

  .landscape {
    position: absolute; left: 0; top: 973px; width: 1200px; height: 955px;
    background: linear-gradient(180deg, #2c7cc6 0%, #6aa9dc 25%, #a9cde9 42%, #b9c9d2 52%, #cfd8dc 58%, #7b8a80 66%, #4e4e45 78%, #3a3631 100%);
  }
  .notch { position: absolute; left: 0; top: 1860px; width: 1200px; height: 70px; }
  .edge-line { position: absolute; left: 0; top: 1928px; width: 4px; height: 245px; background: var(--navy); }

  .contact-frame {
    position: absolute; left: 232px; top: 2029px; width: 736px; height: 286px;
    border: 3px solid #111;
  }
  .contact-label {
    position: absolute; left: 344px; top: 2008px; width: 538px; height: 50px;
    background: var(--navy); color: #fff; font-size: 35px; font-weight: 400;
    display: flex; align-items: center; justify-content: center; line-height: 1;
  }
  .contact-lines { position: absolute; left: 282px; top: 2090px; font-size: 33px; line-height: 50px; font-weight: 400; }
  .social-row {
    position: absolute; left: 400px; top: 2296px; height: 40px; padding: 0 14px;
    background: var(--paper); display: flex; align-items: center; gap: 22px;
  }
  .social-row .find { font-size: 16px; font-weight: 500; letter-spacing: 1px; }
  .social-row .network { font-size: 22px; font-weight: 700; color: #111; line-height: 1; }
</style>
</head>
<body>
<main class="flyer">
  <svg width="0" height="0" style="position:absolute">
    <defs>
      <symbol id="chevron-icon" viewBox="0 0 32 32">
        <circle cx="16" cy="16" r="14" fill="none" stroke="#333" stroke-width="2"/>
        <polyline points="13,10 19,16 13,22" fill="none" stroke="#333" stroke-width="2.4" stroke-linecap="round" stroke-linejoin="round"/>
      </symbol>
    </defs>
  </svg>

  <h1 class="heading">Your Flight</h1>
  <div class="feature" style="left:144px;top:150px"><svg><use href="#chevron-icon"/></svg>One-hour sunrise balloon flight in the spectacular King Valley region in North East Victoria</div>
  <div class="feature" style="left:144px;top:198px"><svg><use href="#chevron-icon"/></svg>Delicious champagne breakfast after the flight (recommended option)</div>
  <div class="feature" style="left:144px;top:245px"><svg><use href="#chevron-icon"/></svg>Informative details throughout your experience with our locally based expert crew</div>
  <div class="feature" style="left:144px;top:293px"><svg><use href="#chevron-icon"/></svg>The opportunity to be involved in the inflation and deflation process should you wish</div>

  <svg class="photo-band" viewBox="0 456 1200 517" preserveAspectRatio="none">
    <defs>
      <linearGradient id="basket-photo" x1="0" y1="0" x2="0" y2="1">
        <stop offset="0" stop-color="#6f6a66"/>
        <stop offset="0.35" stop-color="#c9b08a"/>
        <stop offset="0.6" stop-color="#8a6a48"/>
        <stop offset="1" stop-color="#5b6b4a"/>
      </linearGradient>
    </defs>
    <polygon points="0,456 664,456 400,973 0,973" fill="url(#basket-photo)" role="img" aria-label="Photo of smiling passengers in a balloon basket floating low over a river at sunrise"/>
    <polygon points="688,467 1200,467 1200,973 424,973" fill="#e8f1fa"/>
  </svg>

  <div class="panel-list">
    <div class="feature" style="left:682px;top:568px"><svg><use href="#chevron-icon"/></svg>Safe, friendly and professional</div>
    <div class="feature" style="left:653px;top:626px"><svg><use href="#chevron-icon"/></svg>The flight lasts approximately 1 hour</div>
    <div class="feature" style="left:624px;top:683px"><svg><use href="#chevron-icon"/></svg>The entire experience takes about 3-4 hours</div>
    <div class="feature" style="left:598px;top:738px"><svg><use href="#chevron-icon"/></svg>Suitable from age 7 to 97</div>
    <div class="feature" style="left:570px;top:792px"><svg><use href="#chevron-icon"/></svg>Gift Vouchers are also available</div>
    <div class="feature" style="left:542px;top:846px"><svg><use href="#chevron-icon"/></svg>Contact us for exclusive flight options at your custom location</div>
  </div>

  <div class="landscape" role="img" aria-label="Photo of three colourful hot-air balloons drifting over misty vineyards and a winery at dawn, mountains on the horizon"></div>
  <svg class="notch" viewBox="0 1860 1200 70" preserveAspectRatio="none">
    <polygon points="464,1930 600,1875 736,1930" fill="#ffffff"/>
  </svg>
  <div class="edge-line"></div>

  <div class="contact-frame"></div>
  <div class="contact-label">For bookings or more information:</div>
  <div class="contact-lines">
    <div>www.skylarkaerialtours.com.au</div>
    <div>flights@skylarkaerialtours.com.au</div>
    <div>or call our friendly team on 1300 759 275</div>
  </div>
  <div class="social-row">
    <span class="find">FIND US ON :</span>
    <span class="network">Chatterbook</span>
    <span class="network">Snapframe</span>
    <span class="network">Wayfarer Notes</span>
  </div>
</main>
</body>
</html>
```